Simple elegant business card

General card for a fin and television director.
Just want name, email, phone and address.

Target Market(s)

Prospective employers

Industry/Entity Type

Business

Requirements
Must have
• As above
Nice to have
• Logo but not necessary.
Should not have
• Not too colourful or funky.
• Simplicity and elegance the way to go.

```html
<!DOCTYPE html>
<html lang="en">
<head>
<meta charset="utf-8">
<title>Nora Vance — Business Card</title>
<link rel="stylesheet" href="https://fonts.googleapis.com/css2?family=Fira+Sans:wght@400;600&display=swap">
<style>
  :root {
    --backdrop: #1f1f1f;
    --panel-dark: #3a3a3a;
    --panel-dark-edge: #333333;
    --panel-light: #f1f1f1;
    --accent-gold: #e6a532;
    --accent-gold-light: #efbd4a;
    --name-ink: #ececec;
    --body-ink: #3d3d3d;
  }
  * { box-sizing: border-box; margin: 0; padding: 0; }
  html, body {
    width: 1200px;
    height: 900px;
    overflow: hidden;
    background: var(--backdrop);
  }
  .canvas {
    position: relative;
    width: 1200px;
    height: 900px;
  }
  .business-card {
    position: absolute;
    left: 360px;
    width: 477px;
    height: 269px;
    display: flex;
    font-family: "Fira Sans", sans-serif;
  }
  .business-card--upper { top: 166px; }
  .business-card--lower { top: 476px; }

  .card-identity {
    width: 228px;
    height: 100%;
    background: linear-gradient(180deg, var(--panel-dark) 0%, var(--panel-dark-edge) 100%);
    position: relative;
  }
  .card-name {
    position: absolute;
    left: 60px;
    top: 82px;
    font-size: 21px;
    font-weight: 600;
    color: var(--name-ink);
    letter-spacing: 0.1px;
  }
  .card-accent {
    width: 10px;
    height: 100%;
    background: linear-gradient(180deg, var(--accent-gold-light) 0%, var(--accent-gold) 100%);
  }
  .business-card--lower .card-accent { background: var(--accent-gold); }

  .card-details {
    flex: 1;
    height: 100%;
    background: var(--panel-light);
    position: relative;
    color: var(--body-ink);
  }
  .card-address {
    position: absolute;
    left: 35px;
    top: 87px;
    font-size: 15.5px;
    line-height: 19px;
    font-style: normal;
  }
  .card-contacts {
    position: absolute;
    left: 35px;
    top: 152px;
    list-style: none;
    font-size: 15.5px;
  }
  .contact-item {
    display: flex;
    align-items: center;
    height: 26px;
  }
  .contact-icon {
    width: 15px;
    height: 15px;
    margin-right: 18px;
    fill: var(--body-ink);
  }
</style>
</head>
<body>
<main class="canvas">

  <section class="business-card business-card--upper">
    <div class="card-identity"><h1 class="card-name">Nora Vance</h1></div>
    <div class="card-accent"></div>
    <div class="card-details">
      <address class="card-address">42 Harbor Lane<br>Larkspur, CA 94939</address>
      <ul class="card-contacts">
        <li class="contact-item">
          <svg class="contact-icon" viewBox="0 0 16 16" aria-hidden="true"><path d="M3 1.5l2.5-.5 1.6 3.4-1.5 1.2c.8 1.9 2.3 3.5 4.2 4.4l1.3-1.5 3.4 1.7-.6 2.6c-.2.6-.8 1-1.5.9C6.8 13.1 2.9 9.2 2 3.8c-.1-.9.3-1.8 1-2.3z"/></svg>
          <span>+1 415 555 0182</span>
        </li>
        <li class="contact-item">
          <svg class="contact-icon" viewBox="0 0 16 16" aria-hidden="true"><path d="M1 6.5L8 2l7 4.5V14H1z M2.6 7.1L8 10.4l5.4-3.3L8 3.8z" fill-rule="evenodd"/></svg>
          <span>noravance@mail.com</span>
        </li>
      </ul>
    </div>
  </section>

  <section class="business-card business-card--lower">
    <div class="card-identity"><h2 class="card-name">Nora Vance</h2></div>
    <div class="card-accent"></div>
    <div class="card-details">
      <address class="card-address">42 Harbor Lane<br>Larkspur, CA 94939</address>
      <ul class="card-contacts">
        <li class="contact-item">
          <svg class="contact-icon" viewBox="0 0 16 16" aria-hidden="true"><path d="M3 1.5l2.5-.5 1.6 3.4-1.5 1.2c.8 1.9 2.3 3.5 4.2 4.4l1.3-1.5 3.4 1.7-.6 2.6c-.2.6-.8 1-1.5.9C6.8 13.1 2.9 9.2 2 3.8c-.1-.9.3-1.8 1-2.3z"/></svg>
          <span>+1 415 555 0182</span>
        </li>
        <li class="contact-item">
          <svg class="contact-icon" viewBox="0 0 16 16" aria-hidden="true"><path d="M1 6.5L8 2l7 4.5V14H1z M2.6 7.1L8 10.4l5.4-3.3L8 3.8z" fill-rule="evenodd"/></svg>
          <span>noravance@mail.com</span>
        </li>
      </ul>
    </div>
  </section>

</main>
</body>
</html>
```